" Trabalho de forma autônoma como Coach Executivo. O Coaching executivo pode ser contratado tanto por PJ como por PF. São sessões / reuniões nas quais trabalhamos de forma individual para desenvolvimento da pessoa - desenvolvimento de habilidades, autoconsciência dos pontos fortes e pontos a serem desenvolvidos, para que a pessoa desempenhe seu máximo em sua carreira profissional e atinja o sucesso que ela determinou. O foco do trabalho é o desenvolvimento de competências / habilidades para ela desempenhar seu trabalho e se desenvolver em sua carreira profissional com excelência. Também tem o foco, no Coaching de Carreira, na redefinição dos rumos profissionais de uma pessoa. Discussão de possibilidades de caminhos a serem seguidos e uma reflexão do que aconteceu até o momento. Em ambos os casos, é um processo de autoreflexão mas que já parte para a AÇÃO. Não tem nada de estático, só ficar pensando e divagando em ideias. O ponto é fazer com que a pessoa se mova, saia do lugar, vá buscar seus objetivos. Esse apoio durante o processo também é dado para que a ação efetivamente aconteça. "

```html
<!DOCTYPE html>
<html lang="pt-BR">
<head>
<meta charset="UTF-8">
<title>Helena Moriya Coaching – Pasta</title>
<link rel="stylesheet" href="https://fonts.googleapis.com/css2?family=Cormorant+Garamond:wght@500&family=Arimo&display=swap">
<style>
  :root {
    --stage: #1c1e1e;
    --paper: #ffffff;
    --cover: #2c2d31;
    --flap: #2f3033;
    --flap-edge: #3a3b3e;
    --band: #2d5b68;
    --ink: #3d3d3f;
    --ink-light: #f2f4f5;
  }
  * { margin: 0; padding: 0; box-sizing: border-box; }
  html, body {
    width: 1200px; height: 1200px; overflow: hidden;
    background: var(--stage);
  }
  .folder { position: relative; width: 1200px; height: 1200px; }
  .folder-flap { position: absolute; left: 0; top: 0; }
  .inner-panel {
    position: absolute; left: 132px; top: 247px;
    width: 463px; height: 641px;
    background: var(--paper);
  }
  .cover-panel {
    position: absolute; left: 595px; top: 247px;
    width: 475px; height: 775px;
    background: var(--cover);
  }
  .cover-band {
    position: absolute; left: 0; top: 449px;
    width: 100%; height: 132px;
    background: var(--band);
  }
  .brand {
    position: absolute; left: 0; width: 100%;
    text-align: center;
  }
  .brand-name {
    font-family: "Cormorant Garamond", serif;
    font-weight: 500; font-size: 31px;
    letter-spacing: 1px; line-height: 1;
  }
  .brand-tag {
    font-family: "Cormorant Garamond", serif;
    font-weight: 500; font-size: 10px;
    letter-spacing: 6px; line-height: 1;
    margin-top: 6px; padding-left: 6px;
  }
  .inner-panel .brand { top: 72px; color: var(--ink); }
  .cover-band .brand { top: 44px; color: var(--ink-light); }
  .contact {
    position: absolute; left: 0; bottom: 44px; width: 100%;
    text-align: center;
    font-family: "Arimo", sans-serif;
    font-size: 16px; line-height: 25px; color: #222;
  }
</style>
</head>
<body>
<main class="folder">
  <svg class="folder-flap" width="1200" height="1200" viewBox="0 0 1200 1200">
    <polygon points="132,888 595,888 595,1027 180,1027 150,948" fill="var(--flap)"/>
    <polyline points="132,888 150,948 180,1027" fill="none" stroke="var(--flap-edge)" stroke-width="2"/>
  </svg>

  <section class="inner-panel">
    <div class="brand">
      <div class="brand-name">HELENA MORIYA</div>
      <div class="brand-tag">COACHING</div>
    </div>
    <address class="contact" style="font-style: normal;">
      tel. 11 90000-4100<br>
      Email: h.moriya@mail.com.br<br>
      Perfil: br.perfilpro.com/in/helena-moriya
    </address>
  </section>

  <section class="cover-panel">
    <div class="cover-band">
      <div class="brand">
        <div class="brand-name">HELENA MORIYA</div>
        <div class="brand-tag">COACHING</div>
      </div>
    </div>
  </section>
</main>
</body>
</html>
```